Website Design for an Exciting & Sophisticated Premium CBD Company.

Design a responsive Website with the following goals in mind:
-      Main theme for the site will be based on the Tall Harbor Pebblegate theme.  Please use this when designing for ease of integration.  You can see our current site to gain more insight.  quillorcbd.example
-	Build trust with website visitors with an engaging, informative content driven website, that leads to a conversion of product purchase and repeat business.
-	The website will embody a lifestyle feel and make the visitor identify with the content or emphasize with the life they used to have or believe they can have by using our products
-	The website will allow for super charged SEO and other digital marketing and advertising strategies and tactics used to increase discovery, awareness, and conversion.
Please see additional goals in the uploaded files.

Target Market(s)
Male/Female 25-50
Number of Pages Required
1 page
Font styles to use
Other font styles liked:
- Monserrat is the company Font. Please use throughout. Regular, Bold, Semi-Bold, light
Requirements
Must have
- Please see attached document for this information
Nice to have
Should not have

```html
<!DOCTYPE html>
<html lang="en">
<head>
<meta charset="utf-8">
<title>Quillor CBD</title>
<link href="https://fonts.googleapis.com/css2?family=Montserrat:wght@300;400;500;600;700&display=swap" rel="stylesheet">
<style>
:root{
  --gold:#c49a4c;
  --ink:#1d1d1d;
  --muted:#555;
  --cream:#fcfaf3;
  --blush:#f2d1ba;
  --brown:#654f2c;
  --line:#ececec;
  --card-rose:#f3eff0;
  --card-cream:#fbf8f1;
  --card-mist:#f3f4f3;
  --kraft:#d9c2a6;
}
*{margin:0;padding:0;box-sizing:border-box}
html,body{width:1200px;height:2860px;overflow:hidden}
body{font-family:'Montserrat',sans-serif;color:var(--ink);background:#fff;position:relative}
.abs{position:absolute}
.btn-outline{position:absolute;border:1px solid var(--gold);color:var(--gold);font-size:11px;font-weight:600;letter-spacing:2px;display:flex;align-items:center;justify-content:center;background:transparent}

/* hero */
.hero-left{left:0;top:0;width:600px;height:592px;background:var(--cream)}
.hero-photo{left:600px;top:0;width:600px;height:592px;background:linear-gradient(135deg,#e9ebec 0%,#dfe3e0 35%,#a9c287 60%,#e6e8ea 85%)}
.brand{display:flex;align-items:center;gap:8px;font-weight:500;color:var(--gold);letter-spacing:3px}
.brand .dot{width:14px;height:14px;border-radius:50%;background:var(--gold)}
.nav{left:243px;top:40px;display:flex;gap:36px;font-size:11px;font-weight:600}
.chat{left:970px;top:29px;width:128px;height:36px;background:#fff;font-size:11px;font-weight:600;letter-spacing:1px;display:flex;align-items:center;justify-content:center;gap:8px}
.kicker{left:101px;top:212px;font-size:26px;font-weight:300;letter-spacing:4px}
.headline{left:101px;top:242px;font-size:46px;font-weight:700;letter-spacing:.5px;white-space:nowrap}
.hero-copy{left:103px;top:320px;width:430px;font-size:12px;line-height:22px;color:#333}
.scroll-tab{left:570px;top:552px;width:60px;height:54px;background:#fff;border-radius:0 0 30px 30px;display:flex;align-items:center;justify-content:center}

/* benefits */
.section-title{left:0;width:1200px;text-align:center;font-size:31px;font-weight:600}
.benefit{width:200px;text-align:center;font-size:15px;font-weight:600;line-height:20px}
.benefit svg{display:block;margin:0 auto 16px}
.rule{left:161px;top:920px;width:878px;height:1px;background:var(--line)}

/* drops */
.card{top:1041px;width:278px;height:391px;text-align:center}
.card .bottle{width:60px;height:176px;margin:56px auto 0;border-radius:18px 18px 8px 8px;background:linear-gradient(180deg,#111,#2a2a2a 60%,#111)}
.card h3{font-size:19px;font-weight:400;margin-top:32px}
.card p{font-size:12px;margin-top:12px;color:#333}
.card .price{font-size:22px;font-weight:700;color:var(--gold);margin-top:18px}

/* story */
.blob{border-radius:50%;background:var(--cream)}
.story-photo{left:161px;top:1621px;width:419px;height:413px;background:linear-gradient(135deg,#e7a08d,#d8b48e 40%,#7d8a3c 70%,#5f6b2c)}
.story-paper{left:378px;top:1958px;width:243px;height:140px;background:var(--kraft)}
.story-bottle{left:490px;top:1870px;width:62px;height:262px;border-radius:20px 20px 10px 10px;background:linear-gradient(180deg,#111,#2a2a2a 60%,#111);transform:rotate(22deg)}
.eyebrow{left:671px;top:1660px;font-size:11px;font-weight:600;letter-spacing:2px;color:var(--gold)}
.story-title{left:671px;top:1678px;font-size:46px;font-weight:600}
.story-copy{left:671px;top:1753px;width:360px;font-size:12.5px;line-height:21.6px;color:#333}

/* cares */
.cares{left:0;top:2186px;width:1200px;height:313px;background:var(--blush)}
.cares-photo{left:0;top:2186px;width:420px;height:313px;background:radial-gradient(ellipse at 48% 55%,#5d8a2e 0 22%,#8fb04c 32%,var(--blush) 58%)}
.cares h2{position:absolute;left:523px;top:70px;font-size:29px;font-weight:600}
.cares p{position:absolute;left:523px;top:128px;width:460px;font-size:13.5px;line-height:24.5px}

/* footer */
.news-title{left:163px;top:2543px;font-size:18px;font-weight:600}
.news-sub{left:163px;top:2573px;font-size:12px;color:#666}
.news-form{left:161px;top:2621px;width:291px;height:49px;background:#fff;box-shadow:0 2px 10px rgba(0,0,0,.1);display:flex;align-items:center;padding:0 12px 0 18px;font-size:11px}
.news-form .sub{margin-left:auto;color:var(--gold);font-weight:600;font-size:10.5px}
.contact{left:583px;top:2543px;font-size:12.5px;line-height:26px}
.phone{left:583px;top:2603px;font-size:21px;font-weight:600;color:var(--gold)}
.email{left:583px;top:2640px;font-size:12.5px}
.foot-links{left:795px;top:2540px;font-size:12.5px;line-height:26px;color:#666}
.socials{left:911px;top:2548px;display:flex;gap:8px}
.socials span{width:27px;height:27px;border:1px solid #888;border-radius:50%}
.base{left:0;top:2738px;width:1200px;height:122px;background:var(--brown);color:#c9b48c;text-align:center}
.up-tab{left:566px;top:2716px;width:68px;height:30px;background:var(--brown);border-radius:34px 34px 0 0;display:flex;justify-content:center;align-items:center}
</style>
</head>
<body>

<div class="abs hero-left"></div>
<div class="abs hero-photo" role="img" aria-label="Dark dropper bottle of CBD oil on white marble with fresh hemp leaves and a dish of golden oil"></div>

<div class="abs brand" style="left:102px;top:37px;font-size:17px"><span class="dot"></span>QUILLOR</div>
<nav class="abs nav"><span>SHOP</span><span>DROPS</span><span>TOPICALS</span></nav>
<svg class="abs" style="left:888px;top:37px" width="16" height="18" viewBox="0 0 16 18" fill="none" stroke="#c49a4c" stroke-width="1.6"><path d="M2 6h12l-1 11H3z"/><path d="M5 6V4a3 3 0 0 1 6 0v2"/></svg>
<svg class="abs" style="left:924px;top:37px" width="18" height="18" viewBox="0 0 18 18" fill="none" stroke="#c49a4c" stroke-width="1.6"><circle cx="7.5" cy="7.5" r="5.5"/><path d="M12 12l5 5"/></svg>
<div class="abs chat"><svg width="14" height="12" viewBox="0 0 14 12" fill="none" stroke="#c49a4c" stroke-width="1.5"><path d="M7 11S1 7 1 3.8A2.8 2.8 0 0 1 7 2.6a2.8 2.8 0 0 1 6 1.2C13 7 7 11 7 11z"/></svg>LET'S CHAT</div>

<div class="abs kicker">NATURALLY RELIEVE</div>
<h1 class="abs headline">STRESS &amp; ANXIETY</h1>
<p class="abs hero-copy">QUILLOR is not your everyday CBD, QUILLOR is a lifestyle. Is about incorporating into your daily routine to be the best you. Focus on flavor, effects and only quality ingredients.</p>
<div class="btn-outline" style="left:101px;top:421px;width:152px;height:45px">SHOP NOW</div>
<div class="abs scroll-tab"><svg width="12" height="18" viewBox="0 0 12 18" fill="none" stroke="#c49a4c" stroke-width="1.4"><path d="M6 1v16M1 12l5 5 5-5"/></svg></div>

<h2 class="abs section-title" style="top:668px">Quillor Cares Benefits</h2>
<div class="abs benefit" style="left:212px;top:758px"><svg width="48" height="48" viewBox="0 0 48 48" fill="none" stroke="#c49a4c" stroke-width="1.6"><circle cx="22" cy="22" r="20"/><circle cx="36" cy="36" r="8" fill="#fff"/><path d="M33 39l6-6"/></svg>Zero Thc</div>
<div class="abs benefit" style="left:411px;top:758px"><svg width="48" height="48" viewBox="0 0 48 48" fill="none" stroke="#c49a4c" stroke-width="1.6"><path d="M19 3h10M21 3v15L10 44h28L27 18V3"/><path d="M14 34h20"/></svg>3rd Party Lab<br>Tested</div>
<div class="abs benefit" style="left:611px;top:758px"><svg width="48" height="48" viewBox="0 0 48 48" fill="none" stroke="#c49a4c" stroke-width="1.6"><circle cx="24" cy="24" r="21"/><rect x="16" y="14" width="16" height="22" rx="3"/><path d="M9 9l30 30"/></svg>Free Of Pesticides +<br>Solvents</div>
<div class="abs benefit" style="left:810px;top:750px"><svg width="56" height="60" viewBox="0 0 56 60" fill="none" stroke="#c49a4c" stroke-width="1.6"><circle cx="18" cy="26" r="12"/><path d="M34 2h6v8h-6zM32 12h10v6H32z"/><rect x="30" y="18" width="14" height="38" rx="3"/><circle cx="37" cy="38" r="4"/></svg>Broad Spectrum<br>Hemp Cbd</div>
<div class="abs rule"></div>

<h2 class="abs section-title" style="top:968px">Our Drops</h2>
<div class="abs card" style="left:161px;background:var(--card-rose)"><div class="bottle" role="img" aria-label="Black dropper bottle, mint flavor"></div><h3>QUILLOR CBD</h3><p>Q Rise - Cool Mint Drops</p><div class="price">$84.99</div></div>
<div class="abs card" style="left:462px;background:var(--card-cream)"><div class="bottle" role="img" aria-label="Black dropper bottle, cookie flavor"></div><h3>QUILLOR CBD</h3><p>Q Ease - Vanilla Cookie Drops</p><div class="price">$84.99</div></div>
<div class="abs card" style="left:763px;background:var(--card-mist)"><div class="bottle" role="img" aria-label="Black dropper bottle, berry flavor"></div><h3>QUILLOR CBD</h3><p>Q Unwind - Berry Lemonade Drops</p><div class="price">$84.99</div></div>
<div class="btn-outline" style="left:502px;top:1480px;width:196px;height:45px">SHOP ALL DROPS</div>

<div class="abs blob" style="left:-180px;top:1495px;width:480px;height:480px"></div>
<div class="abs blob" style="left:958px;top:1985px;width:420px;height:420px"></div>
<div class="abs story-photo" role="img" aria-label="Legs resting on a blanket in a field of yellow flowers beside a sun hat and camera"></div>
<div class="abs story-paper" role="img" aria-label="Torn kraft paper under a dropper bottle"></div>
<div class="abs story-bottle" role="img" aria-label="Dropper bottle of CBD oil"></div>
<div class="abs eyebrow">OUR STORIES</div>
<h2 class="abs story-title">QUILLORCBD</h2>
<p class="abs story-copy">Was born out of a drive for a better life. Created to enable the extraordinary in us all through the use of CBD. QUILLOR stands for fun, excitement, joy, and happiness, all the qualities that promote the best feeling and overall wellbeing. QUILLOR's purpose is to provide a more fulfilled life using CBD. Providing high quality compliant CBD products that provide a lifestyle for people to get behind.</p>
<div class="btn-outline" style="left:669px;top:1952px;width:182px;height:45px">DISCOVER MORE</div>

<section class="abs cares"><h2>Quillor Cares?</h2><p>QUILLOR CARES is our non-profit organization created to give back to children and communities in need.&nbsp; We believe that children and giving are keys to our future, which is why we started QUILLORCARES.EXAMPLE (currently under construction).</p></section>
<div class="abs cares-photo" role="img" aria-label="Hemp leaf with small amber oil bottles on a peach background"></div>

<div class="abs news-title">Subscribe to our newsletter</div>
<div class="abs news-sub">Get the latest updates on new products and upcoming sales</div>
<div class="abs news-form"><svg width="14" height="10" viewBox="0 0 14 10" fill="none" stroke="#c49a4c" stroke-width="1.2"><rect x=".6" y=".6" width="12.8" height="8.8"/><path d="M1 1l6 5 6-5"/></svg><span style="margin-left:14px">Enter your Email</span><span class="sub">SUBSCRIBE</span></div>
<div class="abs contact">2480 Alder Court<br>Brookvale TX 70412</div>
<div class="abs phone">555-018-2460</div>
<div class="abs email">social@quillorcbd.example</div>
<div class="abs foot-links">Home<br>Shop<br>Drops<br>Topicals</div>
<div class="abs socials"><span></span><span></span><span></span><span></span></div>

<div class="abs base"><div class="brand" style="justify-content:center;margin-top:44px;font-size:17px;color:#c9b48c">QUILLOR</div><div style="font-size:11px;margin-top:14px">© 2020 Quillor CBD</div></div>
<div class="abs up-tab"><svg width="12" height="18" viewBox="0 0 12 18" fill="none" stroke="#fff" stroke-width="1.4"><path d="M6 17V1M1 6l5-5 5 5"/></svg></div>

</body>
</html>
```